IT services company requires Letterhead design

We need a professional letterhead designed to be used for general correspondence with customers, quotes, invoices etc. We are a new IT services company specialising in computer servicing and repairs and mobile and tablet repairs. Attached are templates that my printing company have supplied, my logos, an interpretation of our website for you to get a feel of the company. Details to be included on the letterhead are

Company Number – 4738261
VAT Number - 518337942
Registered Address – 14-16 Brambly Lane, London, E4 9QT

Phone – 01632 487215
Email – sales@quorvent.com
Web – www.quorvent.com

I would prefer for the top of the letterhead to just have the company logo on a white background and the rest of the details on the bottom of the letterhead but I am open to design ideas.

Thanks

```html
<!DOCTYPE html>
<html lang="en">
<head>
<meta charset="utf-8">
<title>Quorvent Letterhead</title>
<link href="https://fonts.googleapis.com/css2?family=Source+Sans+3:wght@400;700&family=Noto+Serif:wght@400&display=swap" rel="stylesheet">
<style>
  :root {
    --ink: #3b3b3d;
    --brand-blue: #2fc0e8;
    --paper: #ffffff;
    --rule: #555555;
    --watermark: #ededed;
    --backdrop: #f2f2f2;
  }
  * { margin: 0; padding: 0; box-sizing: border-box; }
  html, body {
    width: 934px;
    height: 1200px;
    overflow: hidden;
    background: var(--backdrop);
  }
  .letterhead {
    position: relative;
    width: 934px;
    height: 1200px;
    background: var(--paper);
    font-family: "Source Sans 3", sans-serif;
    color: var(--ink);
  }
  .brand {
    position: absolute;
    left: 22px;
    top: 26px;
    display: flex;
    align-items: center;
    gap: 12px;
  }
  .brand-mark {
    width: 18px;
    height: 18px;
    background: var(--brand-blue);
  }
  .brand-name {
    font-weight: 700;
    font-size: 72px;
    line-height: 1;
    color: var(--ink);
    letter-spacing: -1px;
  }
  .registered-address {
    position: absolute;
    left: 711px;
    top: 42px;
    height: 58px;
    padding-left: 10px;
    border-left: 1px solid var(--rule);
    font-size: 15.5px;
    line-height: 20px;
    display: flex;
    flex-direction: column;
    justify-content: center;
    color: #1e1e1e;
  }
  .watermark {
    position: absolute;
    left: 0;
    right: 0;
    top: 452px;
    text-align: center;
    font-weight: 700;
    font-size: 180px;
    line-height: 1;
    color: var(--watermark);
    letter-spacing: -2px;
  }
  .footer-rule {
    position: absolute;
    left: 0;
    right: 0;
    height: 1px;
    background: var(--rule);
  }
  .footer-rule.top { top: 1110px; }
  .footer-rule.bottom { top: 1150px; }
  .contact-band {
    position: absolute;
    left: 0;
    right: 0;
    top: 1114px;
    height: 31px;
    background: var(--brand-blue);
    color: #ffffff;
    font-family: "Noto Serif", serif;
    font-size: 14.5px;
    display: flex;
    align-items: center;
    justify-content: space-between;
    padding: 0 14px;
    white-space: nowrap;
  }
  .contact-item {
    display: flex;
    align-items: center;
    gap: 7px;
  }
  .divider {
    width: 1px;
    height: 19px;
    background: rgba(255,255,255,0.75);
  }
  .contact-item svg {
    width: 15px;
    height: 15px;
    flex: none;
  }
</style>
</head>
<body>
<main class="letterhead">
  <header>
    <div class="brand">
      <span class="brand-mark"></span>
      <span class="brand-name">Quorvent</span>
    </div>
    <address class="registered-address">
      <span>14-16 Brambly Lane</span>
      <span>London, E4 9QT</span>
    </address>
  </header>

  <div class="watermark" aria-hidden="true">Quorvent</div>

  <footer>
    <div class="footer-rule top"></div>
    <div class="contact-band">
      <span class="contact-item">VAT No. - 518337942</span>
      <span class="divider"></span>
      <span class="contact-item">Company No. – 4738261</span>
      <span class="divider"></span>
      <span class="contact-item">
        <svg viewBox="0 0 16 16" aria-hidden="true"><circle cx="8" cy="8" r="7" fill="none" stroke="#fff" stroke-width="1.2"/><path d="M5.5 4.5c.6-.5 1.2 0 1.5.8l.4 1-1 .8c.4 1 1.1 1.8 2.1 2.3l.8-1 1 .4c.8.3 1.2.9.8 1.5-.6.9-1.7 1-2.7.5-1.8-1-3-2.4-3.5-4.1-.3-1 0-1.7.6-2.2z" fill="#fff"/></svg>
        01632 487215
      </span>
      <span class="divider"></span>
      <span class="contact-item">
        <svg viewBox="0 0 16 16" aria-hidden="true"><rect x="1" y="3.5" width="14" height="9" fill="#fff"/><path d="M1 3.5l7 5 7-5" fill="none" stroke="#2fc0e8" stroke-width="1.2"/></svg>
        sales@quorvent.com
      </span>
      <span class="divider"></span>
      <span class="contact-item">
        <svg viewBox="0 0 16 16" aria-hidden="true"><g fill="none" stroke="#fff" stroke-width="1"><circle cx="8" cy="8" r="6.5"/><ellipse cx="8" cy="8" rx="3" ry="6.5"/><path d="M1.5 8h13M2.5 4.8h11M2.5 11.2h11"/></g></svg>
        www.quorvent.com
      </span>
    </div>
    <div class="footer-rule bottom"></div>
  </footer>
</main>
</body>
</html>
```